TAVRO Capital Group LLC a High Risk Big Rewards company for Rich Young Entrepreneurs

We would like a very modern, powerful in the eyes of our customers, modern, minimalist feel, financial gain. this business card is for young Rich entrepreneurs who want to invest money into High Risk, Big Rewards Businesses. The card Should sell the business!! let your creativity go Wild! I pick most of the designers for this project because of your BOLD Designs, I would like this card to be Bold, Modern, Minimalist, use as many effects in your graphic Artist Mind, Do not let the Financial sound of this business to make you think Conservative that's the last thing we are! if you have a lot of money and you want to play a risky market call US
Updates

Project Deadline Extended
Reason: have not received, enough designs to choose 1st and second place, sure I have received over 100 designs but it seems most designers are submitting every card they have ever made before and calling it mine, please we are looking for fresh ideas please!

Target Market(s)

Private Risky Investors

Industry/Entity Type

Financial

Contact Information for Business Card

powerful in the eyes of our customers,modern, minimalist feel

Font styles to use
Other font styles liked:
• Modern feeling fonts

Requirements
Must have
• The Company Name is TAVRO Capital Group LLC and it must be on the CARD
• My Name, title, Cell , email
• Delvin Ashcroft G.E.D.
• Managing Member
• 555.038.6195
• delvin@tavrocapitalgroup.example
Nice to have
• try a black thick plastic card with round corners with Delvin Ashcroft GED (make sure GED is smaller than name) just on one side of the card, and my phone number with out the icons and email on the other side, this card should look like a exclusive credit card or exclusive VIP card, something you would never loose

```html
<!DOCTYPE html>
<html lang="en">
<head>
<meta charset="utf-8">
<title>TAVRO Capital Group LLC — Business Card</title>
<link rel="stylesheet" href="https://fonts.googleapis.com/css2?family=Barlow:wght@400;500;600&display=swap">
<style>
  :root {
    --backdrop: #d9d5d0;
    --card-black: #050505;
    --card-glow: #363636;
    --gold: #dcb81e;
    --white: #f4f4f4;
    --horizon-line: #c9ccd2;
    --photo-warm: #8a5a14;
    --photo-mid: #3a2408;
    --photo-dark: #0b0a0a;
  }
  * { margin: 0; padding: 0; box-sizing: border-box; }
  html, body {
    width: 1200px;
    height: 1000px;
    overflow: hidden;
    background: var(--backdrop);
    font-family: "Barlow", "Helvetica Neue", Arial, sans-serif;
  }
  .canvas { position: relative; width: 1200px; height: 1000px; }
  .card {
    position: absolute;
    width: 689px;
    height: 393px;
    border-radius: 14px;
    overflow: hidden;
    background:
      radial-gradient(ellipse 300px 200px at 52% 30%, var(--card-glow), transparent 75%),
      var(--card-black);
    box-shadow: 0 6px 16px rgba(0,0,0,0.35);
  }
  .card--back  { left: 261px; top: 92px; }
  .card--front { left: 262px; top: 528px; }
  .card__art { position: absolute; inset: 0; width: 100%; height: 100%; }
  .card__text {
    position: absolute;
    left: 0; right: 0;
    text-align: center;
    white-space: nowrap;
    padding-left: 30px;
  }
  .brand-name {
    color: var(--gold);
    font-weight: 600;
    font-size: 56px;
    letter-spacing: 0.1em;
    line-height: 1;
  }
  .brand-tagline {
    color: var(--gold);
    font-weight: 500;
    font-size: 24px;
    line-height: 1;
  }
  .contact-phone { color: var(--white); font-size: 37px; font-weight: 500; line-height: 1; }
  .contact-email { color: var(--white); font-size: 26px; font-weight: 400; line-height: 1; }
  .holder-name { color: var(--white); font-size: 38px; font-weight: 500; line-height: 1; }
  .holder-name__degree { font-size: 24px; font-weight: 400; }
  .holder-title { color: var(--white); font-size: 26px; font-weight: 400; line-height: 1; }
</style>
</head>
<body>
<div class="canvas">

  <section class="card card--back">
    <svg class="card__art" viewBox="0 0 689 393">
      <defs>
        <linearGradient id="photoToneBack" x1="0" y1="0" x2="1" y2="0">
          <stop offset="0" stop-color="var(--photo-warm)"/>
          <stop offset="0.55" stop-color="var(--photo-mid)"/>
          <stop offset="1" stop-color="var(--photo-dark)"/>
        </linearGradient>
      </defs>
      <path role="img" aria-label="Photograph of a sunrise over the curve of the Earth seen from space"
            d="M0,0 H689 V58 Q220,88 0,253 Z" fill="url(#photoToneBack)"/>
      <path d="M0,253 Q220,88 689,58" fill="none" stroke="var(--horizon-line)" stroke-width="2"/>
    </svg>
    <div class="card__text brand-name" style="top:148px;">TAVRO</div>
    <div class="card__text brand-tagline" style="top:203px;">Capital Group LLC</div>
    <div class="card__text contact-phone" style="top:268px;">555.038.6195</div>
    <div class="card__text contact-email" style="top:310px;">delvin@tavrocapitalgroup.example</div>
  </section>

  <section class="card card--front">
    <svg class="card__art" viewBox="0 0 689 393">
      <defs>
        <linearGradient id="photoToneFront" x1="0" y1="0" x2="1" y2="0">
          <stop offset="0" stop-color="var(--photo-warm)"/>
          <stop offset="0.55" stop-color="var(--photo-mid)"/>
          <stop offset="1" stop-color="var(--photo-dark)"/>
        </linearGradient>
      </defs>
      <path role="img" aria-label="Photograph of a sunrise over the curve of the Earth seen from space"
            d="M0,0 H689 V62 Q230,70 0,258 Z" fill="url(#photoToneFront)"/>
      <path d="M0,258 Q230,70 689,62" fill="none" stroke="var(--horizon-line)" stroke-width="2"/>
    </svg>
    <div class="card__text brand-name" style="top:150px;">TAVRO</div>
    <div class="card__text brand-tagline" style="top:206px;">Capital Group LLC</div>
    <div class="card__text holder-name" style="top:270px;">Delvin Ashcroft <span class="holder-name__degree">G.E.D.</span></div>
    <div class="card__text holder-title" style="top:315px;">Managing Member</div>
  </section>

</div>
</body>
</html>
```